Corvell Upholstery & Design
Stationary & Biz Card
Project: Corvell Upholstery & Design
Corvell Upholstery & Design -
Creative Brief
Bright & Fun-filled
Dorin Velasq
Owner
51847 Pellinore Court Sterling, VA 20166
dorin@corvellupholstery-example.com
www.corvellupholstery-example.com

```html
<!DOCTYPE html>
<html lang="en">
<head>
<meta charset="utf-8">
<title>Corvell Upholstery &amp; Design — Stationery</title>
<link href="https://fonts.googleapis.com/css2?family=Josefin+Sans:wght@300;400&display=swap" rel="stylesheet">
<style>
  :root{
    --red:#e2403f;
    --grey:#8f8f8f;
    --ink:#6b6b6b;
    --paper:#ffffff;
    --stage:#ece6de;
    --shadow:0 2px 5px rgba(0,0,0,.25);
  }
  *{margin:0;padding:0;box-sizing:border-box}
  html,body{width:1200px;height:310px;overflow:hidden}
  body{background:var(--stage);font-family:"Josefin Sans",sans-serif;color:var(--ink);position:relative}
  .piece{position:absolute;background:var(--paper);box-shadow:var(--shadow)}
  .wordmark{font-weight:300;color:var(--red);letter-spacing:.22em;white-space:nowrap;display:flex;align-items:center;gap:.35em}
  .wordmark .dot{display:inline-block;width:.55em;height:.55em;border-radius:50%;background:var(--red)}
  .wordmark.light{color:var(--paper)}
  .wordmark.light .dot{background:var(--paper)}
  .label{position:absolute;font-size:5px;color:#7a726a;white-space:nowrap}
  .tiny{font-size:4px;line-height:1.45;color:var(--ink);white-space:nowrap}

  /* Presentation title */
  .title-block{position:absolute;left:24px;top:30px;width:192px;text-align:center}
  .title-block .wordmark{font-size:22px;justify-content:center}
  .title-block .sub{font-size:7px;letter-spacing:.2em;color:var(--grey);margin-top:6px}
  .title-block .tag{font-size:6px;color:var(--ink);margin-top:8px}

  /* Business cards */
  .card-front{left:17px;top:211px;width:98px;height:46px;padding:8px 6px;display:flex;justify-content:space-between}
  .card-front .wordmark{font-size:7px;align-self:center}
  .card-front .tiny{text-align:right;font-size:3.4px}
  .card-front .name{color:var(--red)}
  .card-logo{left:17px;top:269px;width:93px;height:33px;display:flex;align-items:center;justify-content:center}
  .card-logo .wordmark{font-size:8px}
  .card-back{left:120px;top:269px;width:91px;height:33px;background:var(--red);display:flex;align-items:center;justify-content:center}
  .card-back .wordmark{font-size:8px}

  /* Letterheads */
  .letterhead{top:24px;width:228px;height:269px}
  .letterhead::before{content:"";position:absolute;left:9px;top:0;bottom:0;width:4px;background:var(--red)}
  .letterhead.first{left:223px}
  .letterhead.second{left:497px}
  .letterhead .head{position:absolute;top:16px;left:24px;right:12px;display:flex;justify-content:space-between;align-items:flex-start}
  .letterhead .head .wordmark{font-size:9px}
  .letterhead.second .head{justify-content:center}
  .letterhead .foot{position:absolute;bottom:10px;left:0;right:0;text-align:center;font-size:3.6px}

  /* Envelopes */
  .env{width:163px}
  .env-dl{left:761px;top:79px;height:58px}
  .env-dl::after,.env-front::after{content:"";position:absolute;left:0;right:0;bottom:0;height:3px;background:var(--red)}
  .env-dl .wordmark,.env-front .wordmark{position:absolute;left:8px;top:8px;font-size:6px}
  .env-dl .tiny,.env-front .tiny{position:absolute;left:8px;top:18px;font-size:3px}
  .env-front{left:761px;top:192px;height:84px}
  .env-stack{position:absolute;left:948px;width:228px}
  .env-stack svg{display:block;filter:drop-shadow(0 2px 3px rgba(0,0,0,.25))}
  .env-stack .wordmark{position:absolute;left:50%;transform:translateX(-50%);font-size:7px}
</style>
</head>
<body>

  <header class="title-block">
    <div class="wordmark"><span class="dot"></span>CORVELL</div>
    <div class="sub">UPHOLSTERY &amp; DESIGN</div>
    <div class="tag">Stationary &amp; Biz Card</div>
  </header>

  <!-- Business cards -->
  <section class="piece card-front">
    <div class="wordmark"><span class="dot"></span>CORVELL</div>
    <div class="tiny">
      <div class="name">Dorin Velasq</div>
      <div>Owner</div>
      <div>51847 Pellinore Court</div>
      <div>Sterling, VA 20166</div>
      <div>dorin@corvellupholstery-example.com</div>
      <div>www.corvellupholstery-example.com</div>
    </div>
  </section>
  <section class="piece card-logo"><div class="wordmark">CORVELL</div></section>
  <section class="piece card-back"><div class="wordmark light">CORVELL</div></section>
  <span class="label" style="left:17px;top:304px">Business Cards</span>

  <!-- Letterheads -->
  <section class="piece letterhead first">
    <div class="head">
      <div class="wordmark"><span class="dot"></span>CORVELL</div>
      <div class="tiny" style="text-align:left">
        <div>51847 Pellinore Court</div>
        <div>Sterling, VA 20166</div>
        <div>dorin@corvellupholstery-example.com</div>
        <div>www.corvellupholstery-example.com</div>
      </div>
    </div>
    <div class="foot tiny">Upholstery, drapery and custom furniture</div>
  </section>
  <span class="label" style="left:320px;top:296px">Letterhead</span>

  <section class="piece letterhead second">
    <div class="head"><div class="wordmark"><span class="dot"></span>CORVELL</div></div>
    <div class="foot tiny">Upholstery, drapery and custom furniture</div>
  </section>
  <span class="label" style="left:594px;top:296px">Letterhead</span>

  <!-- Envelopes -->
  <section class="piece env env-dl">
    <div class="wordmark"><span class="dot"></span>CORVELL</div>
    <div class="tiny">51847 Pellinore Court · Sterling, VA 20166</div>
  </section>
  <span class="label" style="left:815px;top:141px">Envelope</span>

  <section class="piece env env-front">
    <div class="wordmark"><span class="dot"></span>CORVELL</div>
    <div class="tiny">51847 Pellinore Court · Sterling, VA 20166</div>
  </section>
  <span class="label" style="left:815px;top:280px">Envelope</span>

  <div class="env-stack" style="top:72px">
    <svg width="228" height="72" viewBox="0 0 228 72" aria-hidden="true">
      <rect width="228" height="72" fill="#ffffff"/>
      <path d="M0 0H228L114 38Z" fill="#8f8f8f"/>
    </svg>
    <div class="wordmark light" style="top:8px;font-size:6px">CORVELL</div>
  </div>
  <div class="env-stack" style="top:132px">
    <svg width="228" height="72" viewBox="0 0 228 72" aria-hidden="true">
      <rect width="228" height="72" fill="#ffffff"/>
      <path d="M0 0H228L114 40Z" fill="#e2403f"/>
    </svg>
    <div class="wordmark light" style="top:9px;font-size:6px">CORVELL</div>
  </div>
  <div class="env-stack" style="top:192px">
    <svg width="228" height="84" viewBox="0 0 228 84" aria-hidden="true">
      <rect width="228" height="84" fill="#ffffff"/>
      <path d="M0 0L114 44L228 0" fill="none" stroke="#dcdcdc" stroke-width="1"/>
      <path d="M0 84L96 36M228 84L132 36" stroke="#e8e8e8" stroke-width="1"/>
    </svg>
    <div class="wordmark" style="top:50px">CORVELL</div>
  </div>
  <span class="label" style="left:1050px;top:280px">Envelopes</span>

</body>
</html>
```